candle postcard

We need a postcard telling customers about our new line of candles to go along with our bath and body product line. We like pretty and clean. dont love clip art.
Like the postcard to say something like:
If you love what Bloom, A Herbarium does for your body, wait until you see what we’ve got in store for your home. We’ve taken 4 popular Aroma Blends: Santorini, Chamomile Flower, Vanilla Plum and Lavender Mint, and transformed them into a range of luxury soy-based candles. Pair a candle with any of our nourishing skin care products to create the ultimate at-home spa experience or give them as the perfect, pampering gift.

For more info or to order:
info@bloomaherbarium-example.com
bloomaherbarium-example.com
800.471.3962

Return address:
418 Fenwick Ave
Dayton, OH 45492

```html
<!DOCTYPE html>
<html lang="en">
<head>
<meta charset="utf-8">
<title>Bloom, A Herbarium — Candle Postcard</title>
<link href="https://fonts.googleapis.com/css2?family=Roboto+Condensed:wght@300;400&display=swap" rel="stylesheet">
<style>
  :root {
    --bg-top: #f4f8f7;
    --bg-bottom: #e3ecee;
    --magenta: #c21fa8;
    --blue: #1f2fc0;
    --mint: #9ef0c8;
    --mint-deep: #7fe6b8;
    --lavender: #b9a6e8;
    --card: rgba(255,255,255,0.82);
  }
  * { margin: 0; padding: 0; box-sizing: border-box; }
  html, body { width: 1200px; height: 923px; overflow: hidden; }
  body {
    font-family: "Roboto Condensed", "Arial Narrow", sans-serif;
    background: linear-gradient(180deg, var(--bg-top) 0%, #eef4f3 45%, var(--bg-bottom) 100%);
  }
  .postcard { position: relative; width: 1200px; height: 923px; overflow: hidden; }

  .petal-art {
    position: absolute; left: 0; top: 0; width: 560px; height: 340px;
    background:
      radial-gradient(ellipse 120px 190px at 70px 150px, rgba(214,196,238,0.75), transparent 70%),
      radial-gradient(ellipse 130px 170px at 190px 250px, rgba(244,210,200,0.7), transparent 70%),
      radial-gradient(ellipse 140px 110px at 430px 150px, rgba(240,244,196,0.75), transparent 70%),
      radial-gradient(ellipse 160px 120px at 420px 40px, rgba(226,244,200,0.6), transparent 70%);
  }
  .spa-photo {
    position: absolute; left: 0; top: 370px; width: 940px; height: 553px;
    background:
      radial-gradient(ellipse 180px 140px at 60px 380px, rgba(190,225,120,0.55), transparent 75%),
      radial-gradient(ellipse 420px 200px at 470px 230px, #ffffff, rgba(255,255,255,0) 80%),
      radial-gradient(ellipse 520px 260px at 420px 330px, rgba(214,222,228,0.9), transparent 80%),
      linear-gradient(180deg, rgba(225,234,238,0) 0%, rgba(222,230,238,0.8) 100%);
  }

  .brand-card {
    position: absolute; left: 28px; top: 0; width: 465px; height: 210px;
    background: var(--card);
    border-bottom: 12px solid var(--mint);
    display: flex; align-items: center; justify-content: center; gap: 16px;
  }
  .brand-card .dot { width: 18px; height: 18px; border-radius: 50%; background: var(--mint-deep); }
  .brand-name { font-weight: 300; font-size: 44px; color: var(--mint-deep); letter-spacing: 1px; }

  .copy p {
    position: absolute; right: 30px; white-space: nowrap; text-align: right;
    height: 50px; line-height: 50px;
  }
  .magenta { color: var(--magenta); }
  .blue { color: var(--blue); }
  .lead { font-weight: 300; font-size: 39px; }
  .body { font-weight: 400; font-size: 29px; }
  .feature { font-weight: 300; font-size: 39px; }
  .mid { font-weight: 300; font-size: 36px; }
  .big { font-weight: 300; font-size: 46px; }

  .contact {
    position: absolute; left: 803px; top: 720px; width: 360px; height: 203px;
    background: rgba(255,255,255,0.88);
    border-top: 13px solid var(--lavender);
    color: var(--blue);
  }
  .contact p {
    position: absolute; left: 0; width: 100%; text-align: center;
    white-space: nowrap; height: 40px; line-height: 40px;
  }
  .contact .label { font-size: 28px; }
  .contact .link { font-size: 23px; }
  .contact .phone { font-weight: 300; font-size: 42px; height: 56px; line-height: 56px; }
</style>
</head>
<body>
<main class="postcard">
  <div class="petal-art" role="img" aria-label="Soft translucent flower petals in lavender, peach and pale yellow"></div>
  <div class="spa-photo" role="img" aria-label="Rolled white towel scattered with pink and blue petals, green tea-light candles, a pink rose, skin care jars and bath salts"></div>

  <header class="brand-card">
    <span class="dot"></span>
    <span class="brand-name">Bloom, A Herbarium</span>
  </header>

  <section class="copy">
    <p class="lead magenta" style="top:20px">If you love what Bloom,</p>
    <p class="lead magenta" style="top:70px">A Herbarium does for your body.</p>
    <p class="body magenta" style="top:110px">Wait until you see what we’ve got in store for your home.</p>

    <p class="body blue" style="top:188px">We’ve taken 4 popular Aroma Blends:</p>
    <p class="feature blue" style="top:237px">Santorini, Chamomile Flower, Vanilla Plum and Lavender Mint</p>
    <p class="body blue" style="top:278px">and transformed them into a range of luxury soy-based candles.</p>

    <p class="body magenta" style="top:360px">Pair a candle with any of</p>
    <p class="body magenta" style="top:398px">our nourishing skin care products to create</p>
    <p class="mid magenta" style="top:447px">the ultimate at-home spa experience</p>
    <p class="body magenta" style="top:487px">or give them as</p>
    <p class="big magenta" style="top:537px">the perfect pampering gift.</p>
  </section>

  <aside class="contact">
    <p class="label" style="top:10px">For more info or to order:</p>
    <p class="link" style="top:50px">info@bloomaherbarium-example.com</p>
    <p class="link" style="top:88px">bloomaherbarium-example.com</p>
    <p class="phone" style="top:130px">800.471.3962</p>
  </aside>
</main>
</body>
</html>
```